Business Card Design

After a corporate career in the finance sector I am now operating on my own as a consultant. I require a simple design, and want a strong card which is targeted at a conservative audience.

Target Market(s)

highly educated senior management, directors of companies, finance sector

Industry/Entity Type

Conservative

Contact Information for Business Card

Rosa Tindell
Consultant
Mobile: 0417 862 254
Email: rosa.tind@mailvora.com

Requirements
Should not have
• I don't want the colours green/yellow/brown

```html
<!DOCTYPE html>
<html lang="en">
<head>
<meta charset="utf-8">
<title>Rosa Tindell – Consultant</title>
<link rel="stylesheet" href="https://fonts.googleapis.com/css2?family=Bitter:wght@700&display=swap">
<style>
  :root {
    --page-bg: #ffffff;
    --card-grey: #cccccc;
    --brand-red: #ed1c24;
    --ink: #000000;
    --on-red: #ffffff;
  }
  html, body {
    margin: 0;
    padding: 0;
    width: 1200px;
    height: 741px;
    overflow: hidden;
    background: var(--page-bg);
  }
  .canvas {
    position: relative;
    width: 1200px;
    height: 741px;
    font-family: "Bitter", Georgia, serif;
    font-weight: 700;
  }
  .card {
    position: absolute;
    left: 70px;
    top: 82px;
    width: 1061px;
    height: 575px;
  }
  .card__identity {
    position: absolute;
    left: 0;
    top: 0;
    width: 100%;
    height: 379px;
    background: var(--card-grey);
  }
  .card__contact {
    position: absolute;
    left: 0;
    top: 379px;
    width: 100%;
    height: 196px;
    background: var(--brand-red);
  }
  .line {
    position: absolute;
    left: 0;
    width: 100%;
    margin: 0;
    text-align: center;
    line-height: 1;
    white-space: nowrap;
  }
  .name {
    top: 199px;
    font-size: 80px;
    color: var(--ink);
    letter-spacing: 1px;
  }
  .name__text {
    display: inline-block;
    border-bottom: 11px solid var(--brand-red);
  }
  .role {
    top: 292px;
    font-size: 57px;
    color: var(--ink);
    letter-spacing: 1px;
  }
  .mobile {
    top: 49px;
    font-size: 50px;
    color: var(--on-red);
    letter-spacing: 1px;
  }
  .email {
    top: 102px;
    font-size: 50px;
    color: var(--on-red);
    letter-spacing: 1px;
  }
</style>
</head>
<body>
  <main class="canvas">
    <section class="card" aria-label="Business card">
      <div class="card__identity">
        <h1 class="line name"><span class="name__text">Rosa Tindell</span></h1>
        <p class="line role">Consultant</p>
      </div>
      <div class="card__contact">
        <p class="line mobile">Mobile: 0417 862 254</p>
        <p class="line email">Email: rosa.tind@mailvora.com</p>
      </div>
    </section>
  </main>
</body>
</html>
```